Innovative tech company looking for a new look for business card

We need a business card revamp- our current design is amazingly dated and in need of a new vision. The Delta is logo that is used, but other than that and the company name - we are open to everything- red is the color of choice typically due to delta. KW is a National credit reporting agency servicing lending institutions for more than 24 years.

***We want a minimal, clean design, we want to move away from the harsh- red, black and white feel. The files uploaded are to show what we are currently using and exactly what we want to move AWAY from.

Thanks you to all!

We are looking for a "lighter" feel more "quorn-esque." We want to move away from the harsh black , white, and red. The files I uploaded were more to show what we currently have and really want to move away from. I am going to edit the brief to be sure this is expressed.

Reason: Still looking for options....

Reason: Still looking for more designs -

```html
<!DOCTYPE html>
<html lang="en">
<head>
<meta charset="utf-8">
<title>Kinwell Ledger – Business Card</title>
<link rel="stylesheet" href="https://fonts.googleapis.com/css2?family=Open+Sans:wght@300;400;600&display=swap">
<style>
  :root {
    --backdrop: #eeece9;
    --card: #fcfbf9;
    --ink: #3b424c;
    --muted: #6b727c;
    --band: #c9ced5;
    --band-edge: #b4bac3;
    --accent: #ef8a80;
  }
  * { margin: 0; padding: 0; box-sizing: border-box; }
  html, body {
    width: 1200px; height: 939px; overflow: hidden;
    background: var(--backdrop);
    font-family: "Open Sans", Arial, sans-serif;
  }
  .card {
    position: absolute; left: 75px; top: 170px;
    width: 1050px; height: 600px;
    background: var(--card);
    overflow: hidden;
    box-shadow: 0 16px 36px rgba(60,66,76,.12);
  }
  .band { position: absolute; left: 0; width: 100%; background: var(--band); }
  .band--top { top: 0; height: 30px; }
  .band--bottom { bottom: 0; height: 42px; }
  .tab { position: absolute; background: var(--accent); border: 3px solid var(--band-edge); }
  .tab--top { top: -3px; left: 52px; width: 300px; height: 46px; border-radius: 0 0 8px 8px; }
  .tab--bottom { bottom: -3px; left: 175px; width: 320px; height: 66px; border-radius: 8px 8px 0 0; }
  .pointer { position: absolute; left: 0; top: 118px; width: 42px; height: 46px; fill: var(--band-edge); }
  .identity { position: absolute; left: 92px; top: 100px; color: var(--ink); }
  .identity__name { font-weight: 400; font-size: 50px; letter-spacing: 1px; line-height: 1; }
  .identity__role { font-weight: 400; font-size: 19px; margin-top: 14px; color: var(--muted); }
  .contacts { position: absolute; left: 92px; top: 262px; list-style: none; color: var(--ink); }
  .contacts__item { display: flex; align-items: center; gap: 16px; font-size: 23px; line-height: 1.3; margin-bottom: 26px; }
  .contacts__icon { width: 26px; height: 26px; flex: none; }
  .contacts__icon--solid { fill: var(--ink); }
  .contacts__icon--line { fill: none; stroke: var(--ink); stroke-width: 1.8; }
  .brand { position: absolute; left: 560px; top: 252px; display: flex; align-items: center; gap: 14px; }
  .brand__mark { width: 30px; height: 30px; background: var(--accent); }
  .brand__name { font-size: 40px; font-weight: 400; color: var(--ink); letter-spacing: 1px; line-height: 1; }
</style>
</head>
<body>
  <div class="card">
    <div class="band band--top"></div>
    <div class="tab tab--top"></div>
    <div class="band band--bottom"></div>
    <div class="tab tab--bottom"></div>

    <svg class="pointer" viewBox="0 0 42 46"><polygon points="0,0 28,0 42,23 28,46 0,46"/></svg>

    <div class="identity">
      <h1 class="identity__name">OMAR HALE</h1>
      <p class="identity__role">Managing Director</p>
    </div>

    <ul class="contacts">
      <li class="contacts__item">
        <svg class="contacts__icon contacts__icon--solid" viewBox="0 0 24 24"><path d="M12 3 2 12h3v9h5v-6h4v6h5v-9h3z"/></svg>
        <span>17 Orchard Row,<br>Eastvale 4410</span>
      </li>
      <li class="contacts__item">
        <svg class="contacts__icon contacts__icon--line" viewBox="0 0 24 24"><circle cx="12" cy="12" r="9.5"/><ellipse cx="12" cy="12" rx="4" ry="9.5"/><line x1="2.5" y1="12" x2="21.5" y2="12"/><line x1="4" y1="7" x2="20" y2="7"/><line x1="4" y1="17" x2="20" y2="17"/></svg>
        <span>omarhale@kinwell-ledger.com<br>kinwell-ledger.com</span>
      </li>
      <li class="contacts__item">
        <svg class="contacts__icon contacts__icon--solid" viewBox="0 0 24 24"><path d="M6.6 2.5 9.5 6.5 7.8 9c1.2 2.7 3.4 5 6.2 6.2l2.5-1.7 4 2.9-1.6 3.6C11 20 4 13 2.9 4.1z"/></svg>
        <span>888-027-340-612-08<br>888-027-340-612-08</span>
      </li>
    </ul>

    <div class="brand">
      <span class="brand__mark"></span>
      <span class="brand__name">Kinwell Ledger</span>
    </div>
  </div>
</body>
</html>
```